Makeup Artist Requires Business Card design

Hi

I am looking for a business card design to market my makeup artist business. I operate under my own name Mara Veldt and I would like to keep the design of the card very simplistic and chic - something that keeps both my name and profession (makeup artist) the focus of the card. I would like it to be a style that is eyecatching to the reader (i am open to anything unusual) but upmarket.

Target Market(s)

women, magazine/beauty/fashion editors, photographers.

Industry/Entity Type

Business

Requirements
Must have
• Must contain:

Phone number: 0418 372 915
Website: www.maraveldt.com.au
email: contact@maraveldt.com.au

(although you don't need to have prefaced these with the words phone number, website etc :))
Should not have
• I am not looking for anything overly colorful - my preference is to keep the card dark if possible.

```html
<!DOCTYPE html>
<html lang="en">
<head>
<meta charset="utf-8">
<title>Mara Veldt – Make-up Artist Business Card</title>
<link rel="stylesheet" href="https://fonts.googleapis.com/css2?family=Pinyon+Script&family=Libre+Baskerville:wght@400;700&display=swap">
<style>
  :root {
    --page-bg: #d9d6d2;
    --card-dark: #141414;
    --card-mid: #2c2c2c;
    --card-light: #6a6a6a;
    --glow: #f4f4f4;
    --text-grey: #8d8d8d;
    --text-soft: #a2a2a2;
    --contact-text: #e8e8e8;
    --contact-halo: #050505;
    --brush-hair: #7a4a2c;
    --brush-hair-dark: #4a2a18;
    --brush-ferrule: #b9b9b9;
  }
  * { margin: 0; padding: 0; box-sizing: border-box; }
  html, body {
    width: 1200px;
    height: 900px;
    overflow: hidden;
    background: var(--page-bg);
  }
  .canvas {
    position: relative;
    width: 1200px;
    height: 900px;
    display: flex;
    align-items: center;
    justify-content: center;
  }
  .business-card {
    position: relative;
    width: 1000px;
    height: 610px;
    overflow: hidden;
    background:
      radial-gradient(ellipse 330px 290px at 790px 230px, var(--glow) 0%, #cfcfcf 30%, var(--card-light) 58%, rgba(60,60,60,0) 100%),
      linear-gradient(200deg, #4a4a4a 0%, var(--card-mid) 35%, var(--card-dark) 80%);
    box-shadow: 0 12px 30px rgba(0,0,0,0.35);
  }
  .brand-name {
    position: absolute;
    left: 52px;
    top: 40px;
    font-family: "Pinyon Script", cursive;
    font-size: 98px;
    line-height: 1;
    color: var(--text-grey);
    white-space: nowrap;
  }
  .profession {
    position: absolute;
    left: 150px;
    top: 182px;
    font-family: "Libre Baskerville", serif;
    font-weight: 700;
    font-size: 31px;
    letter-spacing: 1px;
    color: var(--text-grey);
  }
  .phone {
    position: absolute;
    left: 165px;
    top: 278px;
    font-family: "Libre Baskerville", serif;
    font-size: 50px;
    letter-spacing: 2px;
    color: var(--text-soft);
  }
  .contact-line {
    position: absolute;
    font-family: "Libre Baskerville", serif;
    font-size: 27px;
    color: var(--contact-text);
    text-shadow:
      0 0 3px var(--contact-halo),
      0 0 3px var(--contact-halo),
      0 0 6px var(--contact-halo);
    white-space: nowrap;
  }
  .contact-web { left: 60px; top: 520px; }
  .contact-email { left: 505px; top: 520px; }
  .product-photo {
    position: absolute;
    left: 600px;
    top: 50px;
    width: 390px;
    height: 400px;
  }
</style>
</head>
<body>
  <main class="canvas">
    <section class="business-card">
      <h1 class="brand-name">Mara Veldt</h1>
      <p class="profession">MAKE-UP ARTIST</p>
      <p class="phone">0418 372 915</p>
      <svg class="product-photo" viewBox="0 0 390 400" role="img" aria-label="Photograph of two make-up brushes with brown bristles and silver ferrules">
        <defs>
          <linearGradient id="photo-tone" x1="0" y1="0" x2="1" y2="1">
            <stop offset="0" stop-color="var(--brush-hair)"/>
            <stop offset="0.5" stop-color="var(--brush-hair-dark)"/>
            <stop offset="1" stop-color="var(--brush-ferrule)"/>
          </linearGradient>
        </defs>
        <rect x="20" y="40" width="350" height="330" rx="10" fill="url(#photo-tone)" opacity="0.85"/>
      </svg>
      <p class="contact-line contact-web">www.maraveldt.com.au</p>
      <p class="contact-line contact-email">contact@maraveldt.com.au</p>
    </section>
  </main>
</body>
</html>
```